Business Card Redesign

We would like to redesign our existing business cards.
The new design shall look:
ELEGANT, LUXURY, PROFESSIONAL
Reference:
YOU CAN VISIT WWW.LUMEN-RIVET.HK FOR BETTER UNDERSTANDING OF COMPANY STRATEGY AND POSITION
Additional:
CHOSEN CANDIDATE SHALL PROVIDE THE INSTRUCTION OF PRINTING IF ANY THERMAL COVERAGE OR ANY ADDITION IS OFFERED
Industry/Entity Type
Business

```html
<!DOCTYPE html>
<html lang="en">
<head>
<meta charset="utf-8">
<title>Lumen Rivet Limited – Business Card</title>
<link href="https://fonts.googleapis.com/css2?family=Mulish:wght@400;600;700&display=swap" rel="stylesheet">
<style>
  :root {
    --page: #ffffff;
    --card: #01021f;
    --gold: #e8a321;
    --white: #ffffff;
    --label: #1e5a9c;
    --glow: #3f7fd0;
    --ship: #1d5fa8;
  }
  html, body {
    margin: 0;
    padding: 0;
    overflow: hidden;
  }
  body {
    width: 1118px;
    height: 1200px;
    background: var(--page);
    position: relative;
    font-family: "Mulish", sans-serif;
  }
  .side-label {
    position: absolute;
    left: 95px;
    margin: 0;
    font-size: 21px;
    font-weight: 400;
    color: var(--label);
  }
  .side-label--front { top: 332px; }
  .side-label--back { top: 806px; }

  .card {
    position: absolute;
    left: 258px;
    width: 719px;
    height: 432px;
    background: var(--card);
    overflow: hidden;
  }
  .card--front { top: 114px; }
  .card--back { top: 615px; }

  .brand-glow {
    position: absolute;
    left: 52px;
    top: 58px;
    width: 330px;
    height: 330px;
    border-radius: 50%;
    background: radial-gradient(closest-side, #0a1a4a 0%, #0a1a4a 58%, var(--glow) 72%, rgba(63,127,208,0.35) 85%, rgba(1,2,31,0) 100%);
    transform: rotate(-25deg) scaleY(0.86);
  }
  .brand-mark {
    position: absolute;
    left: 107px;
    top: 196px;
    width: 220px;
    margin: 0;
    text-align: center;
    font-size: 20px;
    font-weight: 600;
    color: var(--white);
  }

  .company {
    position: absolute;
    left: 443px;
    top: 124px;
    margin: 0;
    font-size: 20px;
    font-weight: 400;
    color: var(--white);
    letter-spacing: 0.3px;
  }
  .person-name {
    position: absolute;
    left: 441px;
    top: 183px;
    margin: 0;
    font-size: 28px;
    font-weight: 400;
    color: var(--gold);
  }
  .person-role {
    position: absolute;
    left: 443px;
    top: 218px;
    margin: 0;
    font-size: 15px;
    color: var(--gold);
  }
  .contact {
    position: absolute;
    left: 443px;
    margin: 0;
    color: var(--gold);
  }
  .contact--mobile { top: 253px; font-size: 19px; }
  .contact--email { top: 279px; font-size: 15px; font-weight: 600; }

  .address {
    position: absolute;
    left: 74px;
    top: 129px;
    margin: 0;
    font-style: normal;
    font-size: 16px;
    line-height: 20px;
    color: var(--gold);
  }
  .address .office { display: block; margin-bottom: 6px; }
  .lines {
    position: absolute;
    left: 76px;
    top: 227px;
    margin: 0;
    font-size: 16px;
    line-height: 20px;
    color: var(--gold);
  }
  .website {
    position: absolute;
    left: 76px;
    top: 286px;
    margin: 0;
    font-size: 15px;
    font-weight: 700;
    color: var(--white);
  }
  .ship-art {
    position: absolute;
    left: 388px;
    top: 184px;
    width: 290px;
    height: 246px;
    background: radial-gradient(ellipse at 50% 55%, rgba(29,95,168,0.55) 0%, rgba(29,95,168,0.18) 60%, rgba(1,2,31,0) 100%);
  }
</style>
</head>
<body>
  <p class="side-label side-label--front">Front</p>
  <section class="card card--front">
    <div class="brand-glow"></div>
    <p class="brand-mark">Lumen Rivet Limited</p>
    <p class="company">Lumen Rivet Limited</p>
    <p class="person-name">Daria Voss</p>
    <p class="person-role">PR Consultant</p>
    <p class="contact contact--mobile">(852) 6170 4482</p>
    <p class="contact contact--email">daria@lumen-rivet.hk</p>
  </section>

  <p class="side-label side-label--back">Back</p>
  <section class="card card--back">
    <address class="address">
      <span class="office">Headquarters (Hong Kong)</span>
      Rm. 1204B, 12/F, Harlow Centre,<br>
      58 Wyndham Lane, Central,<br>
      Hong Kong
    </address>
    <p class="lines">Tel&nbsp; : (852) 2460-3318<br>Fax : (852) 2460-3310</p>
    <p class="website">www.lumen-rivet.hk</p>
    <div class="ship-art" role="img" aria-label="Blue line drawing of a sailing junk boat"></div>
  </section>
</body>
</html>
```